Leaf Haven Business Card Design

My E-Commerce store is called Leaf Haven

Website address is - http://www.leafhaven-demo.com.au

I would like a colourful, friendly business with the description in the 'must haves' box incorporated into it
Updates

Please add the following to the business cards; Natural & Organic Products Online Organic Pantry Items Superfoods & Supplements Natural Skincare Eco Friendly Household Products

Industry/Entity Type

Business

Contact Information for Business Card

www.leafhaven-demo.com.au
mira@leafhaven-demo.com.au

Colors
acd037
9bcb3c
cadf82
eaf2ce

Requirements
Must have
• Natural & Organic Eco Products Online.
• Leaf Haven specialises in organic pantry items, superfoods and supplements, organic skincare for you and your family & eco friendly household products.

```html
<!DOCTYPE html>
<html lang="en">
<head>
<meta charset="utf-8">
<title>Leaf Haven Business Card</title>
<link href="https://fonts.googleapis.com/css2?family=Open+Sans:wght@400;600;700&display=swap" rel="stylesheet">
<style>
  :root {
    --page-bg: #efece6;
    --card-white: #ffffff;
    --green: #5dbb63;
    --green-deep: #1fa34a;
    --green-light: #b7ddab;
    --green-pale: #d9eed2;
    --ink: #3d3d3d;
    --ink-soft: #4a4a4a;
    --divider: #d6d6d6;
  }
  * { margin: 0; padding: 0; box-sizing: border-box; }
  html, body {
    width: 1200px; height: 1127px; overflow: hidden;
    background: var(--page-bg);
    font-family: "Open Sans", Arial, sans-serif;
  }
  .canvas { position: relative; width: 1200px; height: 1127px; }

  .card {
    position: absolute; width: 838px; height: 478px;
    border-radius: 44px; overflow: hidden;
    box-shadow: 0 2px 6px rgba(0,0,0,0.18);
  }
  .card-front { left: 60px; top: 55px; background: var(--card-white); }
  .card-back {
    left: 304px; top: 583px;
    background: radial-gradient(ellipse 60% 70% at 50% 40%, var(--green-light) 0%, #86c97f 45%, var(--green-deep) 100%);
  }

  .wave { position: absolute; left: 0; top: 0; width: 838px; height: 478px; }

  .brand-mark {
    position: absolute; border-radius: 50%;
    background: var(--green-pale);
    display: flex; align-items: center; justify-content: center;
  }
  .card-front .brand-mark { left: 99px; top: 47px; width: 296px; height: 296px; }
  .card-back .brand-mark { left: 279px; top: 40px; width: 280px; height: 280px; background: rgba(255,255,255,0.35); }
  .brand-name {
    font-size: 44px; font-weight: 400; color: var(--green-deep);
    line-height: 1; white-space: nowrap;
  }

  .divider {
    position: absolute; left: 437px; top: 98px; width: 2px; height: 202px;
    background: var(--divider);
  }

  .contact-list { position: absolute; left: 482px; top: 112px; list-style: none; }
  .contact-list li {
    display: flex; align-items: center; gap: 9px;
    font-size: 20px; color: var(--ink-soft); height: 34px;
  }
  .contact-list svg { width: 19px; height: 19px; flex: none; }

  .address {
    position: absolute; left: 483px; top: 232px;
    font-size: 20px; line-height: 33px; color: var(--ink-soft);
  }

  .person { position: absolute; right: 48px; top: 393px; text-align: right; }
  .person-name { font-size: 28px; font-weight: 700; color: var(--ink); line-height: 36px; }
  .person-title { font-size: 22px; color: var(--ink); letter-spacing: 1px; padding-right: 52px; line-height: 32px; }

  .back-tagline {
    position: absolute; left: 0; width: 100%; top: 333px; text-align: center;
    color: var(--ink-soft);
  }
  .back-tagline .lead { font-size: 17px; font-weight: 600; line-height: 24px; }
  .back-tagline .range { font-size: 14px; line-height: 22px; }

  .back-url {
    position: absolute; left: 0; width: 100%; top: 398px; text-align: center;
    font-size: 26px; letter-spacing: 3.5px; color: var(--ink-soft);
  }
</style>
</head>
<body>
<div class="canvas">

  <section class="card card-front">
    <svg class="wave" viewBox="0 0 838 478" aria-hidden="true">
      <path d="M0,300 C110,385 220,455 330,457 C480,458 610,372 838,343 L838,478 L0,478 Z" fill="var(--green)"/>
      <path d="M0,305 C70,360 130,410 185,440" fill="none" stroke="var(--green-deep)" stroke-width="10"/>
      <path d="M0,338 C70,385 130,418 185,440" fill="none" stroke="#fff" stroke-width="5"/>
      <path d="M590,392 C680,355 760,333 838,328" fill="none" stroke="var(--green-deep)" stroke-width="10"/>
      <path d="M590,392 C680,365 760,350 838,345" fill="none" stroke="#fff" stroke-width="5"/>
    </svg>

    <div class="brand-mark"><span class="brand-name">Leaf Haven</span></div>

    <div class="divider"></div>

    <ul class="contact-list">
      <li>
        <svg viewBox="0 0 20 20"><circle cx="10" cy="10" r="8.5" fill="none" stroke="var(--green-deep)" stroke-width="1.6"/><path d="M7,5.5 L9,7.5 L8,9 C8.6,10.4 9.6,11.4 11,12 L12.5,11 L14.5,13 L13,14.5 C9.5,14.3 5.7,10.5 5.5,7 Z" fill="var(--green-deep)"/></svg>
        000-555-0142
      </li>
      <li>
        <svg viewBox="0 0 20 20"><path d="M2,8 L10,3 L18,8 L18,17 L2,17 Z" fill="var(--green-deep)"/><path d="M2,8 L10,13 L18,8" fill="none" stroke="#fff" stroke-width="1.5"/></svg>
        mira@leafhaven-demo.com.au
      </li>
      <li>
        <svg viewBox="0 0 20 20"><g fill="none" stroke="var(--green-deep)" stroke-width="1.4"><circle cx="10" cy="10" r="8"/><ellipse cx="10" cy="10" rx="3.5" ry="8"/><path d="M2,10 H18 M3.5,6 H16.5 M3.5,14 H16.5"/></g></svg>
        www.leafhaven-demo.com.au
      </li>
    </ul>

    <p class="address">Street Name, City Name<br>Zipcode-012345</p>

    <div class="person">
      <p class="person-name">Your Name</p>
      <p class="person-title">Title</p>
    </div>
  </section>

  <section class="card card-back">
    <div class="brand-mark"><span class="brand-name">Leaf Haven</span></div>
    <div class="back-tagline">
      <p class="lead">Natural &amp; Organic Eco Products Online</p>
      <p class="range">Organic Pantry Items · Superfoods &amp; Supplements · Natural Skincare · Eco Friendly Household Products</p>
    </div>
    <p class="back-url">www.leafhaven-demo.com.au</p>
  </section>

</div>
</body>
</html>
```